Nonprofit serving disconnected/homeless young adults (age 18-24) needs marketing

There are over 5 Million young adults in the U.S. who are neither working nor in school. Many of them 'aged out' of foster care or group homes, meaning the state doesn't provide care for them when they become an adult at age 18. These young adults have slipped through the cracks of society. Many are homeless, which often times leads to drug use, crime, young pregnancy, violence and prison. VANTA is a nonprofit dedicated to providing young adults opportunities, resources and experiences to begin building a life they value. We do that via two channels: one our 6-month living program, where participants live expense-free. The requirement is they work full-time, and save at least 75% of their income. At the end of the 6 months, they have the money needed to get into their own place, along with starter furniture and household basics. All potential candidates for housing program come from the resource center VANTAConnect. It's where VANTA offers immediate assistance to young adults, and in-turn we get to know them, and them us. This is essential to see if they're a fit for the housing program. The marketing piece is something young adults (and members of the community) receive. It should 1) be eye catching, maybe something like a path or a road with a phrase "have you chosen the path you're on?" "if given the chance, would you choose something different?" "this is your opportunity to get serious about what matters most to you" "want something different for you life, here's your chance" ...something to that effect. I want the graphics to be big, in your face, something eye catching.

After that, something that says: "here's how"
1. EVERYTHING IN LIFE STARTS WITH THE FIRST STEP: attend orientation on Tuesday if you haven't already
2. YOU WANT TO SOMETHING DIFFERENT FOR YOUR LIFE, YOU NEED TO DO SOMETHING DIFFERENT: our classes are it.
3. YOU WANT TO BE SUCCESSFUL? HANG OUT WITH LIKE-MINDED INDIVIDUALS: attend a volunteer day or fun activity.

(I uploaded our Logo and our new t-shirt design so you can get a look/feel of our current marketing. it should be somewhat modern, "cool" because we're talking to young adults and again - modern design with large graphics.)

```html
<!DOCTYPE html>
<html lang="en">
<head>
<meta charset="utf-8">
<title>VANTA – Here's How</title>
<link rel="stylesheet" href="https://fonts.googleapis.com/css2?family=Kreon:wght@300;400;500;700&display=swap">
<style>
  :root {
    --teal: #47b99a;
    --teal-bright: #4fc9a6;
    --mint: #93d1bc;
    --mint-line: #7fbfa9;
    --ink: #1d2622;
    --forest: #1f5a45;
    --photo-dark: #26282a;
    --photo-mid: #55585a;
    --footer: #121212;
    --white: #ffffff;
  }
  * { margin: 0; padding: 0; box-sizing: border-box; }
  html, body { width: 989px; height: 1200px; overflow: hidden; background: #e9e9e9; }
  .flyer {
    position: relative; width: 989px; height: 1200px; overflow: hidden;
    font-family: "Kreon", Georgia, serif; background: var(--mint);
  }
  .hero-photo {
    position: absolute; left: 0; top: 0; width: 989px; height: 560px;
    background: radial-gradient(ellipse at 25% 40%, var(--photo-mid) 0%, var(--photo-dark) 70%);
  }
  .brand { position: absolute; left: 428px; top: 50px; display: flex; align-items: center; gap: 12px; }
  .brand-mark { width: 76px; height: 94px; background: var(--teal); }
  .brand-name { font-size: 66px; font-weight: 700; color: var(--teal); letter-spacing: 2px; line-height: 1; }
  .brand-tagline {
    position: absolute; left: 412px; top: 164px; font-size: 8.5px; letter-spacing: 1px;
    color: #d9d9d9;
  }
  .hero-headline {
    position: absolute; left: 412px; top: 213px; width: 575px;
    font-size: 41px; line-height: 45px; font-weight: 400; color: var(--white); text-transform: uppercase;
  }
  .hero-headline .accent { color: var(--teal); }
  .hero-headline .aside { font-size: 23px; text-transform: none; color: var(--teal); margin-left: 10px; }
  .social { position: absolute; left: 412px; top: 435px; display: flex; gap: 4px; }
  .social span { width: 28px; height: 28px; border-radius: 50%; background: var(--teal-bright); display: block; }
  .torn { position: absolute; left: 0; width: 989px; }
  .planks {
    position: absolute; left: 0; top: 500px; width: 989px; height: 600px;
    background: repeating-linear-gradient(to bottom, transparent 0 54px, var(--mint-line) 54px 56px);
  }
  .step-title {
    position: absolute; left: 0; top: 574px; width: 989px; text-align: center;
    font-size: 70px; line-height: 72px; font-weight: 500; color: var(--ink); text-transform: uppercase; letter-spacing: 1px;
  }
  .step-sub {
    position: absolute; left: 0; top: 713px; width: 989px; text-align: center;
    font-size: 28px; line-height: 36px; color: var(--forest);
  }
  .story {
    position: absolute; left: 55px; top: 767px; width: 880px; text-align: center;
    font-size: 17px; line-height: 21px; color: var(--ink); font-weight: 300;
  }
  .story p + p { margin-top: 21px; }
  .story strong { font-weight: 500; }
  .footer {
    position: absolute; left: 0; top: 1080px; width: 989px; height: 120px;
    background: radial-gradient(ellipse at 50% 40%, #4a4a4a 0%, var(--footer) 60%);
  }
  .footer-title {
    position: absolute; left: 0; top: 1115px; width: 989px; text-align: center;
    font-size: 26.5px; line-height: 32px; color: var(--teal); text-transform: uppercase; letter-spacing: .5px;
  }
  .footer-contact {
    position: absolute; left: 0; top: 1150px; width: 989px; text-align: center;
    font-size: 21px; line-height: 26px; color: var(--teal); letter-spacing: .5px;
  }
</style>
</head>
<body>
<main class="flyer">
  <div class="hero-photo" role="img" aria-label="Photo of a young man in a grey hoodie and jeans sitting hunched with his head on his knees against a dark weathered wall"></div>

  <div class="brand">
    <span class="brand-mark"></span>
    <span class="brand-name">VANTA</span>
  </div>
  <p class="brand-tagline">Purpose. Growth. Courage. Belonging. Hope.</p>

  <h1 class="hero-headline">
    You want to something<br>
    <span class="accent">different</span> for your life,<br>
    you need to do something<br>
    different <span class="aside">our classes are it</span>
  </h1>

  <div class="social" aria-label="Social links"><span></span><span></span><span></span></div>

  <div class="planks"></div>

  <svg class="torn" style="top:490px" width="989" height="70" viewBox="0 0 989 70" aria-hidden="true">
    <polygon fill="var(--mint)" points="0,40 30,32 60,38 90,30 120,36 150,24 180,30 210,18 240,26 270,20 300,28 330,22 360,30 390,26 420,34 450,36 470,50 500,58 530,52 560,48 600,50 640,46 680,44 720,40 760,34 800,28 840,20 880,16 920,14 960,10 989,6 989,70 0,70"/>
    <polyline fill="none" stroke="var(--white)" stroke-width="5" points="0,40 30,32 60,38 90,30 120,36 150,24 180,30 210,18 240,26 270,20 300,28 330,22 360,30 390,26 420,34 450,36 470,50 500,58 530,52 560,48 600,50 640,46 680,44 720,40 760,34 800,28 840,20 880,16 920,14 960,10 989,6"/>
  </svg>

  <h2 class="step-title">Everything in life starts<br>with the first step</h2>
  <p class="step-sub">attend orientation on Tuesday if you haven't already</p>

  <div class="story">
    <p>There are over 5 Million young adults in the U.S. who are neither working nor in school. Many of them 'aged out' of foster care or group homes, meaning the state doesn't provide care for them when they become an adult at age 18. These young adults have slipped through the cracks of society. Many are homeless, which often times leads to drug use, crime, young pregnancy, violence and prison.</p>
    <p>VANTA is a nonprofit dedicated to providing young adults opportunities, resources and experiences to begin building a life they value. We do that via two channels: one our 6-month living program, where participants live expense-free. The requirement is they work full-time, and save at least 75% of their income. At the end of the 6 months, they have the money needed to get into their own place, along with starter furniture and household basics. All potential candidates for housing program come from the resource center <strong>VANTAConnect</strong>. It's where VANTA offers immediate assistance to young adults, and in-turn we get to know them, and them us.</p>
  </div>

  <div class="footer"></div>
  <svg class="torn" style="top:1050px" width="989" height="50" viewBox="0 0 989 50" aria-hidden="true">
    <polygon fill="#1a1a1a" points="0,42 40,36 80,38 120,30 160,32 200,22 240,16 280,12 320,18 360,22 400,26 440,24 480,30 520,28 560,32 600,28 640,30 680,34 720,32 760,28 800,30 840,24 880,28 920,22 960,24 989,18 989,50 0,50"/>
    <polyline fill="none" stroke="var(--white)" stroke-width="5" points="0,42 40,36 80,38 120,30 160,32 200,22 240,16 280,12 320,18 360,22 400,26 440,24 480,30 520,28 560,32 600,28 640,30 680,34 720,32 760,28 800,30 840,24 880,28 920,22 960,24 989,18"/>
  </svg>

  <p class="footer-title">You want to be successful? Hang out with like-minded individuals</p>
  <p class="footer-contact">attend a volunteer day or fun activity: chooseVANTA.com | 555 014 0192</p>
</main>
</body>
</html>
```